Progressive/contemporary business card design for successful Startups as a Service Company

New logo launched in 2020. New website launched in 2021. Now that COVID is (mostly) behind us, I'm networking with more people and need a business card that matches the company/logo design aesthetic.

```html
<!DOCTYPE html>
<html lang="en">
<head>
<meta charset="utf-8">
<title>Northvane Business Card</title>
<link rel="stylesheet" href="https://fonts.googleapis.com/css2?family=Montserrat:wght@400;500;700&display=swap">
<style>
  :root {
    --bg-top: #e4e3e1;
    --bg-bottom: #b3b2ae;
    --card: #ffffff;
    --ink: #2c2c2c;
    --brand-navy: #3d4a5e;
    --name-green: #4aa83f;
    --icon-orange: #f26a21;
    --edge: linear-gradient(90deg, #9cc43c 0%, #1e76c7 35%, #8a4fb0 55%, #e3197d 78%, #ee2b2b 100%);
    --divider: linear-gradient(180deg, #a8c94a 0%, #4a7fd0 45%, #9a4fc0 70%, #f0206e 100%);
  }
  * { box-sizing: border-box; margin: 0; padding: 0; }
  html, body { width: 1200px; height: 801px; overflow: hidden; }
  body {
    background: radial-gradient(ellipse at 30% 10%, var(--bg-top) 0%, #cfcecb 45%, var(--bg-bottom) 100%);
    font-family: "Montserrat", sans-serif;
    position: relative;
  }
  .card {
    position: absolute;
    top: 250px;
    width: 530px;
    height: 303px;
    background: var(--card);
    box-shadow: 0 18px 30px rgba(0,0,0,0.22), 0 2px 4px rgba(0,0,0,0.15);
  }
  .card::after {
    content: "";
    position: absolute;
    left: 0; right: 0; bottom: 0;
    height: 4px;
    background: var(--edge);
  }
  .card--info { left: 50px; }
  .card--front { left: 620px; }

  .wordmark {
    display: flex;
    align-items: center;
    gap: 10px;
    font-weight: 500;
    color: var(--brand-navy);
    letter-spacing: 0.22em;
    text-transform: uppercase;
  }
  .wordmark__mark {
    width: 14px; height: 14px;
    background: var(--brand-navy);
  }
  .card--info .wordmark {
    position: absolute;
    left: 34px; top: 138px;
    font-size: 21px;
  }
  .card--front .wordmark {
    position: absolute;
    left: 0; right: 0; top: 128px;
    justify-content: center;
    font-size: 36px;
    gap: 16px;
  }
  .card--front .wordmark__mark { width: 22px; height: 22px; }

  .divider {
    position: absolute;
    left: 262px; top: 62px;
    width: 1px; height: 180px;
    background: var(--divider);
  }
  .contact {
    position: absolute;
    left: 284px; top: 66px;
    color: var(--ink);
    font-size: 12.5px;
    line-height: 1.42;
  }
  .contact__name {
    color: var(--name-green);
    font-weight: 700;
    font-size: 19px;
    letter-spacing: 0.01em;
    text-transform: uppercase;
    line-height: 1.1;
  }
  .contact__role { font-size: 13px; margin-bottom: 14px; }
  .contact__address { margin-bottom: 8px; }
  .contact__line { display: flex; align-items: center; gap: 7px; }
  .contact__icon { width: 11px; height: 11px; flex: none; }
</style>
</head>
<body>
  <section class="card card--info" aria-label="Business card, contact side">
    <div class="wordmark"><span>Northvane</span><span class="wordmark__mark"></span></div>
    <div class="divider"></div>
    <div class="contact">
      <p class="contact__name">Dalen Marsh</p>
      <p class="contact__role">Owner/CEO</p>
      <p class="contact__address">418 Harbor Row<br>Elmsford County 7720</p>
      <p class="contact__line">
        <svg class="contact__icon" viewBox="0 0 12 12" aria-hidden="true"><path fill="var(--icon-orange)" d="M2.4 0.8l2 2-1.1 1.5c.7 1.5 1.9 2.7 3.4 3.4l1.5-1.1 2 2-1.3 2.2C4.6 10.6 1.4 7.4.2 2.1z"/></svg>
        555-018-2746
      </p>
      <p class="contact__line">
        <svg class="contact__icon" viewBox="0 0 12 12" aria-hidden="true"><rect x="0.5" y="2" width="11" height="8" fill="var(--icon-orange)"/><path d="M0.8 2.4L6 6.6l5.2-4.2" fill="none" stroke="#fff" stroke-width="1.1"/></svg>
        hello@northvane.com
      </p>
      <p class="contact__line">
        <svg class="contact__icon" viewBox="0 0 12 12" aria-hidden="true"><circle cx="6" cy="6" r="5.5" fill="var(--icon-orange)"/><path d="M0.8 6h10.4M6 0.6c-2.4 3-2.4 7.8 0 10.8M6 0.6c2.4 3 2.4 7.8 0 10.8" fill="none" stroke="#fff" stroke-width="0.9"/></svg>
        www.northvane.com
      </p>
    </div>
  </section>

  <section class="card card--front" aria-label="Business card, logo side">
    <div class="wordmark"><span>Northvane</span><span class="wordmark__mark"></span></div>
  </section>
</body>
</html>
```